依頼詳細
デザインは、リニューアルした公式ホームページ(https://mori-tone.jp/)とかけ離れていない程度で作成いただきたいです。
既存のチラシは黒基調のデザインで、公式ページとイメージがかけ離れてしまい、チラシを見たお客様が公式ページに訪れた際に違和感を感じてしまう懸念があります。
そういった懸念がなくなるようなデザインでお願いします。

記載項目や掲載してほしい内容については既存のチラシとほぼ同じです。
表面はサーバーを目立たせたいので、詳細情報は裏面に記載するようにお願いします。

データ納品時はこちらが指定したテンプレートにて納品をお願いいたします。
テンプレートは添付ファイルをご確認ください。
記載項目
記載項目はすべて既存チラシの内容を使用してください。
一部修正をお願いしたい箇所がありますので、【修正箇所】モリトーンチラシ.PDFに記載いたします。
既存チラシのaiデータもありますが容量が大きかったため、必要であれば下記からDLをお願いします。
https://kumobako.jp/download/8f41c0d93b7e25a1f6c08d47e2b95a13c7d6e084
サイズ
A4
ページ数
両面
希望イメージ
シンプル 複雑
単色 カラフル
暗い 明るい
日常 高級
遊び心 厳粛
未来的 伝統的
女性的 男性的
希望する色
青系、水色系
納品ファイル
• イラストレーター形式 (.ai)
• フォトショップ形式 (.psd)
補足説明
資料の添付が出来ていなかったようです。
■ 選んだ理由

こちらが依頼した内容をよくご理解いただけているデザインだと思います。シンプルかつ分かりやすく、現在の公式LPに寄せたさわやかなデザインをありがとうございました。

■ 提案者全員のお礼・コメント

たくさんのご応募をいただきありがとうございました。締め切りから当選までお時間がかかってしまい、ご応募いただいたタスカーの皆様にはお時間を頂戴してしまい大変失礼いたしました。
どのデザインも素敵でしたが、社内で一番人気のあったデザインを採用させていただきました。
ありがとうございました。

```html
<!DOCTYPE html>
<html lang="ja">
<head>
<meta charset="utf-8">
<title>Lumo by MORI TONE</title>
<link href="https://fonts.googleapis.com/css2?family=Noto+Sans+JP:wght@400;500;700;900&family=Playfair+Display:wght@400;500&family=Montserrat:wght@500;600;700&family=Zen+Kurenaido&display=swap" rel="stylesheet">
<style>
:root{
  --sky:#cfe8f7;
  --sky-deep:#8fc7ec;
  --blue:#3a8fd6;
  --navy:#1f5fa8;
  --ink:#2b4a6b;
  --pink:#ef6fa6;
  --white:#ffffff;
  --server-white:#f3f5f7;
  --server-black:#1d1e22;
}
*{margin:0;padding:0;box-sizing:border-box}
html,body{width:846px;height:1200px;overflow:hidden;background:var(--white)}
.flyer{
  position:relative;width:846px;height:1200px;overflow:hidden;
  background:
    linear-gradient(115deg,transparent 30%,rgba(255,255,255,.55) 31%,rgba(255,255,255,.55) 33%,transparent 34%),
    linear-gradient(115deg,transparent 60%,rgba(255,255,255,.5) 61%,rgba(255,255,255,.5) 62.5%,transparent 63.5%),
    radial-gradient(ellipse at 20% 25%,var(--sky-deep) 0%,transparent 55%),
    radial-gradient(ellipse at 85% 75%,var(--sky-deep) 0%,transparent 50%),
    var(--sky);
  font-family:"Noto Sans JP",sans-serif;color:var(--ink);
}
.tagline-band{
  position:absolute;top:36px;left:268px;width:338px;height:48px;
  background:var(--blue);color:var(--white);
  font-weight:700;font-size:24px;letter-spacing:.06em;
  display:flex;align-items:center;justify-content:center;
}
.badge-new{
  position:absolute;top:72px;left:16px;width:140px;height:140px;border-radius:50%;
  background:var(--pink);color:var(--white);
  font-family:"Montserrat",sans-serif;font-weight:600;font-size:38px;letter-spacing:.04em;
  display:flex;align-items:center;justify-content:center;
}
.product-name{
  position:absolute;top:200px;left:230px;width:430px;text-align:center;
  font-family:"Playfair Display",serif;font-weight:400;font-size:140px;line-height:1;color:var(--ink);
}
.product-by{
  position:absolute;top:352px;left:230px;width:430px;text-align:center;
  font-family:"Montserrat",sans-serif;font-weight:600;font-size:28px;color:var(--ink);letter-spacing:.02em;
}
.drop{position:absolute}
.server{position:absolute;top:400px;width:142px;height:730px;border-radius:10px 10px 4px 4px}
.server--white{left:268px;background:linear-gradient(90deg,#dfe3e7,var(--server-white) 40%,#e4e7ea)}
.server--black{left:432px;background:linear-gradient(90deg,#0e0f12,var(--server-black) 45%,#2a2c31)}
.copy-vertical{
  position:absolute;writing-mode:vertical-rl;white-space:nowrap;
  background:var(--white);font-weight:700;font-size:27px;letter-spacing:.05em;line-height:1;
  padding:12px 8px;color:var(--ink);
}
.copy-vertical em{font-style:normal;color:var(--pink)}
.copy-vertical--1{left:766px;top:172px}
.copy-vertical--2{left:716px;top:196px}
.bubble{
  position:absolute;top:635px;left:14px;width:190px;height:190px;border-radius:50%;
  background:var(--navy);color:var(--white);
  font-weight:700;font-size:28px;line-height:1.5;text-align:center;
  display:flex;align-items:center;justify-content:center;
}
.always{
  position:absolute;top:790px;left:200px;white-space:nowrap;
  font-family:"Zen Kurenaido",sans-serif;font-size:124px;line-height:1;color:var(--pink);
}
.price{position:absolute;top:935px;right:28px;color:var(--pink);display:flex;align-items:flex-end}
.price__label{
  writing-mode:vertical-rl;font-weight:700;font-size:22px;line-height:1;background:var(--pink);color:var(--white);
  padding:4px 4px;margin-right:6px;margin-bottom:6px;
}
.price__amount{font-family:"Montserrat",sans-serif;font-weight:700;font-size:64px;line-height:1}
.price__yen{font-weight:700;font-size:32px;line-height:1;margin-left:2px;margin-bottom:4px}
.price-tax{position:absolute;top:1012px;right:28px;font-size:18px;color:var(--ink)}
.colors{
  position:absolute;top:1058px;right:28px;
  font-family:"Montserrat",sans-serif;font-weight:700;font-size:22px;color:var(--ink);letter-spacing:.03em;
}
</style>
</head>
<body>
<main class="flyer">
  <div class="tagline-band">ウォーターサーバー新時代</div>
  <div class="badge-new">NEW</div>

  <svg class="drop" style="left:160px;top:270px" width="44" height="62" viewBox="0 0 40 56"><path d="M20 2 C20 2 2 28 2 37 a18 18 0 0 0 36 0 C38 28 20 2 20 2Z" fill="var(--blue)"/></svg>
  <svg class="drop" style="left:40px;top:520px" width="66" height="92" viewBox="0 0 40 56"><path d="M20 2 C20 2 2 28 2 37 a18 18 0 0 0 36 0 C38 28 20 2 20 2Z" fill="var(--blue)"/></svg>
  <svg class="drop" style="left:770px;top:790px" width="44" height="62" viewBox="0 0 40 56"><path d="M20 2 C20 2 2 28 2 37 a18 18 0 0 0 36 0 C38 28 20 2 20 2Z" fill="var(--blue)"/></svg>

  <h1 class="product-name">Lumo</h1>
  <p class="product-by">By MORI TONE</p>

  <div class="server server--white" role="img" aria-label="ホワイトのウォーターサーバー本体の写真"></div>
  <div class="server server--black" role="img" aria-label="ブラックのウォーターサーバー本体の写真"></div>

  <p class="copy-vertical copy-vertical--1">これからは、<em>定額使い放題</em>の</p>
  <p class="copy-vertical copy-vertical--2"><em>ハイブリッド</em>ウォーターサーバーを。</p>

  <div class="bubble">どれだけ<br>使っても、</div>

  <p class="always">ず〜っと</p>

  <div class="price">
    <span class="price__label">月額</span>
    <span class="price__amount">3,980</span>
    <span class="price__yen">円</span>
  </div>
  <p class="price-tax">(税込 4,378円)</p>
  <p class="colors">WHITE / BLACK</p>
</main>
</body>
</html>
```